Business Card Design Project

We consult with hotels on setting rates and maximizing a revenue strategy

Industry/Entity Type

Business

Contact Information for Business Card

I am not sure what I want. Our company offers high level consulting to hotels around the country but we are also laid back. I would like something that is professional but also shows the laid back side

```html
<!DOCTYPE html>
<html lang="en">
<head>
<meta charset="utf-8">
<title>Harborline Business Card</title>
<link href="https://fonts.googleapis.com/css2?family=Open+Sans:wght@400;600;700&display=swap" rel="stylesheet">
<style>
  :root {
    --backdrop: #ece8e3;
    --espresso: #33241f;
    --paper: #ffffff;
    --teal: #3e8f8c;
    --teal-light: #8cc5c1;
    --ink: #3a3330;
    --shadow: rgba(40, 28, 20, 0.22);
  }
  * { margin: 0; padding: 0; box-sizing: border-box; }
  html, body { width: 1200px; height: 900px; overflow: hidden; }
  body {
    background: var(--backdrop);
    font-family: "Open Sans", Arial, sans-serif;
    position: relative;
  }
  .card {
    position: absolute;
    top: 295px;
    width: 540px;
    height: 309px;
    border-radius: 4px;
    box-shadow: 0 10px 26px var(--shadow);
    overflow: hidden;
  }
  .card--back { left: 40px; background: var(--espresso); }
  .card--front { left: 620px; background: var(--paper); }

  .brand {
    position: absolute;
    display: flex;
    flex-direction: column;
  }
  .brand__name {
    font-weight: 700;
    letter-spacing: 1px;
    line-height: 1;
  }
  .brand__tagline {
    font-weight: 600;
    line-height: 1.2;
  }
  .card--back .brand {
    left: 0; right: 0; top: 118px;
    align-items: center;
    color: var(--paper);
  }
  .card--back .brand__name { font-size: 36px; }
  .card--back .brand__tagline { font-size: 13px; margin-top: 6px; }

  .card--front .brand {
    right: 34px; top: 30px;
    align-items: flex-start;
    color: var(--espresso);
  }
  .card--front .brand__name { font-size: 27px; }
  .card--front .brand__tagline {
    font-size: 11px;
    margin-top: 3px;
    padding: 2px 8px;
    background: var(--espresso);
    color: var(--paper);
  }

  .feature-art {
    position: absolute;
    left: 44px; top: 22px;
    width: 170px; height: 287px;
    background: linear-gradient(180deg, var(--teal-light) 0%, var(--teal) 100%);
  }

  .contact {
    position: absolute;
    left: 266px; top: 122px;
    color: var(--ink);
  }
  .contact__name {
    font-size: 19px;
    font-weight: 600;
    color: var(--teal);
  }
  .contact__role {
    font-size: 13px;
    margin-top: 1px;
  }
  .contact__list {
    list-style: none;
    margin-top: 24px;
    font-size: 13px;
  }
  .contact__list li {
    display: flex;
    align-items: center;
    gap: 9px;
    line-height: 21px;
  }
  .contact__list svg { width: 12px; height: 12px; fill: var(--espresso); flex: none; }
</style>
</head>
<body>
  <section class="card card--back" aria-label="Business card back">
    <div class="brand">
      <span class="brand__name">HARBORLINE</span>
      <span class="brand__tagline">Revenue Management Solutions</span>
    </div>
  </section>

  <section class="card card--front" aria-label="Business card front">
    <div class="feature-art" role="img" aria-label="Teal illustration of a gothic suspension bridge tower"></div>

    <div class="brand">
      <span class="brand__name">HARBORLINE</span>
      <span class="brand__tagline">Revenue Management Solutions</span>
    </div>

    <div class="contact">
      <p class="contact__name">Dana Whitfield</p>
      <p class="contact__role">Regional Revenue Manager</p>
      <ul class="contact__list">
        <li>
          <svg viewBox="0 0 12 12" aria-hidden="true"><path d="M2.4 0.8l2 2-1 1.3c.7 1.6 1.9 2.8 3.5 3.5l1.3-1 2 2-1.2 1.6C5.5 9.8 2.2 6.5 0.8 2z"/></svg>
          555-014-2207
        </li>
        <li>
          <svg viewBox="0 0 12 12" aria-hidden="true"><path d="M3 1h5v3H3z M1 4.5h10V11H1z" /><rect x="3" y="6.5" width="6" height="1" fill="#fff"/><rect x="3" y="8.5" width="6" height="1" fill="#fff"/></svg>
          555-014-8861
        </li>
        <li>
          <svg viewBox="0 0 12 12" aria-hidden="true"><path d="M0.5 2.5h11v7h-11z"/><path d="M1 3l5 3.6L11 3" stroke="#fff" stroke-width="1" fill="none"/></svg>
          Dana@HarborlineRMS.com
        </li>
        <li>
          <svg viewBox="0 0 12 12" aria-hidden="true"><circle cx="6" cy="6" r="5.5"/><path d="M1 6h10M6 0.5c-2 2.5-2 8.5 0 11M6 0.5c2 2.5 2 8.5 0 11" stroke="#fff" stroke-width="0.8" fill="none"/></svg>
          www.HarborlineRMS.com
        </li>
      </ul>
    </div>
  </section>
</body>
</html>
```